Holistic Therapy (aromatherapy, massage, reflexology, life coaching, soul healing, aura reading)

I work for myself as a holistic therapist doing: aromatherapy massage, massage, reflexology, abdominal-sacral massage, life coaching, soul healing, aura readings. I want a business card that doesn't focus on any one of these( so not just feet or a massage couch,but rather a card that creates the feeling of wholeness, healing, health and which can encompass all my therapies - e.g. green or purple are colours I like (especially green, or maybe green on back and purple on front). It's going to be called Rosa Elwin Therapies. I don't want to list all my therapies on the card in case I add others later.). At some point I will create a website but in this instance I just want to get some cards printed to get 'out there' while I design my website.
Updates

Hi, thanks for all your designs. Can you find a way to include the therapies that I offer within the card, either on the front or back…the therapies I offer are: aromatherapy massage, reflexology, swedish body massage, abdominal-sacral massage, nutrition, soul healing, aura readings. (Maybe have them with a bullet point before each?) I am not sure whether they should be on the front of the card or the back or whether having them would spoil the card but it occurred to me that just having rosa elwin therapies doesn't tell people what therapies I offer, hence the new idea to list them somehow…)

Target Market(s)

Mainly women (middle class probably with disposable incomes).

Industry/Entity Type

Massage

Contact Information for Business Card

Rosa Elwin Therapies, Tel: 07942 586113, email: vitalbloom@mailvane.com, (on back of card I want: Rosalind Elwin BScHons, OKQRB, GPCL.)

Requirements
Nice to have
• A logo for Rosa Elwin Therapies would be good.

```html
<!DOCTYPE html>
<html lang="en">
<head>
<meta charset="utf-8">
<title>Rosa Elwin Therapies – Business Card</title>
<link href="https://fonts.googleapis.com/css2?family=Open+Sans:wght@400;700&family=Quicksand:wght@500&display=swap" rel="stylesheet">
<style>
  :root {
    --stage: #e9e7e4;
    --card-dark: #232323;
    --card-dark-edge: #1a1a1a;
    --card-light: #ffffff;
    --leaf: #8dc63f;
    --leaf-deep: #62b42d;
    --leaf-mist: rgba(160, 210, 120, 0.32);
    --plum: #7a2e87;
    --plum-mist: rgba(110, 45, 120, 0.55);
    --ink: #2b2b2b;
    --ink-soft: #444444;
  }
  * { margin: 0; padding: 0; box-sizing: border-box; }
  html, body {
    width: 1200px;
    height: 800px;
    overflow: hidden;
    background: var(--stage);
  }
  .stage {
    position: relative;
    width: 1200px;
    height: 800px;
    display: flex;
    align-items: center;
    justify-content: center;
    gap: 70px;
  }
  .card {
    border-radius: 22px;
    box-shadow: 0 12px 30px rgba(0,0,0,0.18);
    position: relative;
    overflow: hidden;
  }
  .card__wash {
    position: absolute;
    inset: 0;
  }

  /* Front */
  .card--front {
    width: 340px;
    height: 540px;
    background: linear-gradient(160deg, #2c2c2c 0%, var(--card-dark) 55%, var(--card-dark-edge) 100%);
  }
  .card--front .card__wash {
    background: radial-gradient(ellipse 70% 45% at 45% 38%, var(--plum-mist) 0%, rgba(110,45,120,0.18) 55%, transparent 80%);
  }
  .brand {
    position: absolute;
    left: 175px;
    top: 300px;
    transform: translate(-50%, -50%) rotate(90deg);
    display: flex;
    align-items: center;
    gap: 26px;
    white-space: nowrap;
  }
  .brand__dot {
    width: 54px;
    height: 54px;
    border-radius: 50%;
    background: var(--plum);
    flex: none;
  }
  .brand__name {
    font-family: "Quicksand", sans-serif;
    font-weight: 500;
    font-size: 30px;
    line-height: 1.25;
    letter-spacing: 2px;
    color: var(--leaf);
  }
  .brand__name span { display: block; }
  .brand__name .upper { text-transform: uppercase; }

  /* Back */
  .card--back {
    width: 540px;
    height: 340px;
    background: var(--card-light);
    font-family: "Open Sans", sans-serif;
  }
  .card--back .card__wash {
    background: radial-gradient(ellipse 60% 70% at 62% 55%, var(--leaf-mist) 0%, rgba(160,210,120,0.12) 55%, transparent 85%);
  }
  .holder {
    position: absolute;
    top: 70px;
    left: 0;
    right: 0;
    text-align: center;
    font-weight: 700;
    font-size: 21px;
    color: var(--leaf-deep);
  }
  .contact {
    position: absolute;
    top: 118px;
    left: 0;
    right: 0;
    text-align: center;
    font-size: 19px;
    line-height: 1.4;
    color: var(--ink);
  }
  .therapies {
    position: absolute;
    bottom: 36px;
    left: 30px;
    right: 20px;
    font-size: 14.5px;
    line-height: 1.55;
    color: var(--ink-soft);
  }
</style>
</head>
<body>
  <main class="stage">
    <section class="card card--front" aria-label="Card front">
      <div class="card__wash" role="img" aria-label="Soft plum background decoration"></div>
      <div class="brand">
        <span class="brand__dot"></span>
        <p class="brand__name"><span class="upper">Rosa Elwin</span><span>Therapies</span></p>
      </div>
    </section>

    <section class="card card--back" aria-label="Card back">
      <div class="card__wash" role="img" aria-label="Soft green background decoration"></div>
      <p class="holder">Rosalind Elwin BScHons, OKQRB, GPCL</p>
      <p class="contact">07942 586113<br>vitalbloom@mailvane.com</p>
      <p class="therapies">
        Aromatherapy Massage | Reflexology | Swedish Body Massage<br>
        Abdominal-sacral Massage | Nutrition | Soul Healing | Aura Readings
      </p>
    </section>
  </main>
</body>
</html>
```